Lonestar Canopy Services, INC Roof Safety Info Marketing Material

We need a flyer to illustrate roof safety methods we offer with the pictures and descriptions uploaded. We are a Dallas-based commercial roofing company named Lonestar Canopy Services, INC.
We would like to incorporate our dark blues (seen on our website logo). The final design should communicate roof safety and our ability to assess any roof system based on their safety needs.
https://brellwaytops.com/company/about-brellway-tops-inc/

Target Market(s)

Construction industry

Industry/Entity Type

Commercial Roofind

Font styles to use
Serif

```html
<!DOCTYPE html>
<html lang="en">
<head>
<meta charset="utf-8">
<title>Lonestar Canopy Services, INC – Roof Safety Flyer</title>
<link href="https://fonts.googleapis.com/css2?family=Bebas+Neue&family=Montserrat:wght@700;800;900&family=Arimo:wght@400;700&family=Tinos:wght@700&display=swap" rel="stylesheet">
<style>
:root{
  --navy:#1f3d80;
  --navy-deep:#1b3672;
  --red:#e5232b;
  --ink:#1a1a1a;
  --paper:#ffffff;
  --stage:#000000;
}
*{box-sizing:border-box;margin:0;padding:0}
html,body{width:1200px;height:1178px;overflow:hidden;background:var(--stage)}
.flyer{position:absolute;left:240px;top:68px;width:740px;height:1048px;background:var(--paper);overflow:hidden;font-family:"Arimo",Arial,sans-serif;color:var(--ink)}
.hero-photo{position:absolute;left:0;top:0;width:740px;height:470px;
  background:linear-gradient(180deg,rgba(255,255,255,0) 55%,#fff 100%),
  linear-gradient(120deg,#e9eef4 0%,#c9d3de 35%,#9aa3ab 60%,#d8dde2 80%,#f1f3f5 100%)}
.brand{position:absolute;left:0;top:0;width:232px;height:122px;background:var(--paper);display:flex;align-items:flex-end;justify-content:center;padding-bottom:12px}
.brand-name{font-family:"Tinos",Georgia,serif;font-weight:700;font-size:13px;color:var(--navy-deep);letter-spacing:.2px}
.falls-block{position:absolute;left:0;top:322px;width:312px;height:118px}
.falls-word{position:absolute;left:26px;top:330px;font-family:"Bebas Neue",Impact,sans-serif;font-size:118px;line-height:1;color:#fff;letter-spacing:1px}
.cause-band{position:absolute;left:0;top:440px;width:740px;height:68px;background:var(--red)}
.cause-text{position:absolute;left:27px;top:454px;font-family:"Montserrat",Arial,sans-serif;font-weight:800;font-size:19.5px;line-height:21px;color:#fff;text-transform:uppercase}
.body-copy{position:absolute;left:27px;width:392px;font-size:13.3px;line-height:15px;text-align:justify}
.body-copy u{font-weight:700}
.intro{top:526px}
.priority{position:absolute;left:27px;top:644px;font-family:"Montserrat",Arial,sans-serif;font-weight:800;font-size:13.5px;line-height:15px;text-transform:uppercase}
.priority .blue{color:var(--navy)}
.priority .red{color:var(--red)}
.inspection{top:690px}
.promise{position:absolute;left:25px;top:812px;width:394px;height:98px;border:1.5px solid var(--red);padding:10px 10px 0 92px;font-size:13.1px;line-height:15px;text-align:justify}
.promise .goal{color:var(--red);font-weight:700}
.promise b{font-weight:700}
.care-icon{position:absolute;left:10px;top:12px;width:72px;height:72px;background:#e9edf6;border-radius:6px}
.info-panel{position:absolute;left:448px;top:322px;width:276px;height:588px;background:var(--navy);border:1px solid #9fb0d6;color:#fff}
.info-title{position:absolute;left:0;width:276px;text-align:center;font-family:"Montserrat",Arial,sans-serif;font-weight:900;text-transform:uppercase}
.info-title.top{top:12px;font-size:25px}
.info-title.sub{top:42px;font-size:18.5px}
.info-rule{position:absolute;left:20px;top:67px;width:240px;height:2px;background:var(--red)}
.icon-slot{position:absolute;background:rgba(255,255,255,.14);border-radius:4px}
.info-text{position:absolute;left:17px;width:242px;font-size:13.1px;line-height:15px;text-align:justify}
.credits{position:absolute;right:21px;top:922px;font-size:9.5px;color:var(--ink)}
.call-band{position:absolute;left:0;top:944px;width:740px;height:38px;background:var(--navy);color:#fff;font-family:"Arimo",Arial,sans-serif;font-weight:700;font-size:15.5px;line-height:38px;text-align:center;letter-spacing:.3px}
.contact-band{position:absolute;left:0;top:982px;width:740px;height:66px;background:var(--red)}
.phone-block{position:absolute;left:0;top:982px;width:740px;height:56px}
.contact-line{position:absolute;left:22px;color:#fff;display:flex;align-items:center;gap:8px}
.contact-line.addr{top:994px;font-size:13.5px}
.contact-line.web{top:1012px;font-size:20px}
.phone-number{position:absolute;left:482px;top:985px;font-family:"Bebas Neue",Impact,sans-serif;font-size:46px;line-height:50px;color:#fff;letter-spacing:1.5px}
.phone-icon{position:absolute;left:440px;top:994px}
</style>
</head>
<body>
<main class="flyer">
  <div class="hero-photo" role="img" aria-label="Photo of a roofer in a hard hat and safety harness balancing on steel roof framing against a bright sky"></div>

  <div class="brand"><span class="brand-name">LONESTAR CANOPY SERVICES, INC</span></div>

  <svg class="falls-block" viewBox="0 0 312 118" aria-hidden="true"><polygon points="0,0 262,0 312,118 0,118" fill="#1f3d80"/></svg>
  <h1 class="falls-word">FALLS</h1>

  <div class="cause-band"></div>
  <p class="cause-text">Are the leading cause of death<br>in the construction industry</p>

  <p class="body-copy intro">Roofers encounter many hazards on the job, including dangers associated with working at great heights with power tools, electricity, noise, and extreme temperatures. A lack of fall protection, damaged fall protection equipment, or improper setup can drastically increase a roofer's risk of falling. Unless these hazards are mitigated by the property owner or employer, roofers are at risk for serious injury or death.</p>

  <h2 class="priority"><span class="blue">At Lonestar Canopy Services,</span><br><span class="red">Safety is our main priority.</span></h2>

  <p class="body-copy inspection">Throughout our inspection, our roofing experts assess your building, identifying three main areas of safety protocol. These areas include <u>evidence of rooftop anchorage</u> to provide safe access to your roof, <u>fall protection systems</u> to allow employees and workers to safely operate on your roof, and <u>protection around fall hazards</u> on your rooftop such as skylights, mechanical or ladder areas.</p>

  <div class="promise">
    <div class="care-icon" role="img" aria-label="Icon of open hands holding a hard hat"></div>
    Following our inspection, our team will thoroughly review and recommend a fall prevention plan that is tailored to your specific needs. <span class="goal">Our goal is</span> <b>to provide you with a system that is safe, OSHA compliant &amp; easy to use.</b>
  </div>

  <aside class="info-panel">
    <h2 class="info-title top">Pertinent Info</h2>
    <h3 class="info-title sub">For Roof Anchors:</h3>
    <div class="info-rule"></div>

    <div class="icon-slot" role="img" aria-label="Icon of a falling worker" style="left:52px;top:88px;width:52px;height:48px"></div>
    <svg style="position:absolute;left:114px;top:104px" width="36" height="24" viewBox="0 0 36 24" aria-hidden="true"><path d="M2 8h18V2l14 10-14 10v-6H2z" fill="#e5232b"/></svg>
    <div class="icon-slot" role="img" aria-label="Icon of a building with its owner" style="left:166px;top:88px;width:64px;height:62px"></div>

    <p class="info-text" style="top:172px">The most important thing (fairly new), if there is an accident on a building, the building owner is responsible for that accident. Previously it fell on the property manager.</p>

    <div class="icon-slot" role="img" aria-label="Icon of a guard rail" style="left:42px;top:258px;width:64px;height:54px"></div>
    <div class="icon-slot" role="img" aria-label="Icon of a roof anchor" style="left:174px;top:254px;width:48px;height:54px"></div>

    <p class="info-text" style="top:336px">OSHA guidelines outlined it. Anything with mechanical equipment or any work within 15 feet of a building edge over 6 feet off the ground. Either guard rails or roof anchors. Its all dependent on your specific situation which is where we come into play. We can make that assessment.</p>

    <div class="icon-slot" role="img" aria-label="Icon of a skylight" style="left:44px;top:466px;width:64px;height:60px"></div>
    <svg style="position:absolute;left:122px;top:476px" width="40" height="40" viewBox="0 0 40 40" aria-hidden="true"><circle cx="20" cy="20" r="19" fill="#e5232b"/><rect x="17.5" y="8" width="5" height="17" rx="1.5" fill="#fff"/><circle cx="20" cy="31" r="3" fill="#fff"/></svg>
    <div class="icon-slot" role="img" aria-label="Icon of a roof hatch" style="left:176px;top:466px;width:64px;height:60px"></div>

    <p class="info-text" style="top:546px;text-align:left">Skylights are a fall-hazard to consider. Roof hatches as well.</p>
  </aside>

  <p class="credits">Icons by Linebrook Studio, Oakpixel, Tern Lab from Iconvale.com</p>

  <div class="call-band">For more &nbsp;information on how we can ensure the safety of your roof, CALL US TODAY!</div>

  <div class="contact-band"></div>
  <svg class="phone-block" viewBox="0 0 740 56" aria-hidden="true"><polygon points="400,0 740,0 740,56 420,56" fill="#1f3d80"/></svg>

  <p class="contact-line addr">
    <svg width="12" height="16" viewBox="0 0 12 16" aria-hidden="true"><path d="M6 0a6 6 0 0 0-6 6c0 4.5 6 10 6 10s6-5.5 6-10a6 6 0 0 0-6-6zm0 8.5A2.5 2.5 0 1 1 6 3.5a2.5 2.5 0 0 1 0 5z" fill="#fff"/></svg>
    415 Carvel Way Garland, TX 75040
  </p>
  <p class="contact-line web">
    <svg width="14" height="14" viewBox="0 0 14 14" aria-hidden="true"><circle cx="7" cy="7" r="6" fill="none" stroke="#fff" stroke-width="1.5"/><path d="M1 7h12M7 1c-3 3-3 9 0 12M7 1c3 3 3 9 0 12" fill="none" stroke="#fff" stroke-width="1.2"/></svg>
    www.brellwaytops.com
  </p>

  <svg class="phone-icon" width="30" height="30" viewBox="0 0 24 24" aria-hidden="true"><path d="M6.6 10.8a15.1 15.1 0 0 0 6.6 6.6l2.2-2.2a1 1 0 0 1 1-.25 11.4 11.4 0 0 0 3.6.57 1 1 0 0 1 1 1V20a1 1 0 0 1-1 1A17 17 0 0 1 3 4a1 1 0 0 1 1-1h3.5a1 1 0 0 1 1 1c0 1.25.2 2.45.57 3.57a1 1 0 0 1-.25 1z" fill="#e5232b"/></svg>
  <p class="phone-number">(972) 555-0148</p>
</main>
</body>
</html>
```